Screendesign für neue Website
Zielgruppe
Bauherren und alle die mal zum Architekten müssen.
Aufgabenstellung
Bei diesem Auftrag handelt es sich um die Erstellung eines Screendesigns für eine Website eines Archtiktenbüros.
Es wird daher ein Layout im PSD-Format erwartet, eine Umsetzung dessen in HTML wird nicht gefordert.

```html
<!DOCTYPE html>
<html lang="de">
<head>
<meta charset="utf-8">
<title>Planungsbüro Anton Weidler – Architekten schaffen</title>
<link href="https://fonts.googleapis.com/css2?family=Caveat:wght@500&family=Open+Sans:wght@400;600&display=swap" rel="stylesheet">
<style>
  :root {
    --bg: #2b2a29;
    --footer: #3b3a39;
    --band: rgba(110, 110, 110, 0.55);
    --script: #f3efc4;
    --text: #ece7d4;
    --nav-top: #6d7073;
    --nav-bottom: #46484b;
    --nav-text: #d9dadb;
    --nav-active-top: #8a8d90;
    --nav-active-bottom: #5a5c5f;
    --nav-active-text: #1f1f1f;
  }
  * { box-sizing: border-box; margin: 0; padding: 0; }
  html, body { width: 1200px; height: 960px; overflow: hidden; background: var(--bg); }
  .page { position: relative; width: 1200px; height: 960px; background: var(--bg); font-family: "Open Sans", Arial, sans-serif; }

  .gallery { position: absolute; top: 0; left: 0; width: 1200px; height: 186px; }
  .gallery .photo { position: absolute; top: 0; width: 185px; height: 186px; }
  .photo--house1 { left: 14px;  background: linear-gradient(180deg, #3f7fd0 0%, #8a5a40 55%, #3f6a2a 100%); }
  .photo--house2 { left: 212px; background: linear-gradient(180deg, #5a8fd8 0%, #e8e6e0 50%, #3f7a2d 100%); }
  .photo--house3 { left: 410px; background: linear-gradient(180deg, #d9dde6 0%, #3d6a2a 40%, #b0533f 60%, #4b7a3a 100%); }
  .photo--office { left: 608px; background: linear-gradient(180deg, #9ab8d8 0%, #2f6a8f 45%, #5d7f86 75%, #4b7a30 100%); }
  .photo--tower  { left: 806px; background: linear-gradient(180deg, #4f86c9 0%, #b7cde3 45%, #5a7a9a 100%); }
  .photo--winter { left: 1004px; background: linear-gradient(180deg, #5f93d6 0%, #e9ecef 40%, #8c8f92 100%); }
  .gallery .band { position: absolute; left: 0; top: 128px; width: 1200px; height: 58px; background: var(--band); }

  .claim { position: absolute; left: 0; top: 0; color: var(--script); }
  .claim__script { position: absolute; font-family: "Caveat", cursive; font-weight: 500; white-space: nowrap; line-height: 1; }
  .claim__headline { left: 30px; top: 220px; font-size: 84px; }
  .claim__final { left: 476px; top: 510px; font-size: 78px; }
  .claim__line { position: absolute; font-size: 22px; color: var(--text); white-space: nowrap; }
  .claim__line--raum { left: 317px; top: 350px; }
  .claim__line--traum { left: 400px; top: 435px; }

  .nav { position: absolute; left: 804px; top: 196px; list-style: none; }
  .nav__item { position: absolute; left: 0; width: 186px; height: 56px; display: flex; align-items: center; justify-content: center;
    background: linear-gradient(180deg, var(--nav-top), var(--nav-bottom)); color: var(--nav-text); font-size: 17px; }
  .nav__item--active { background: linear-gradient(180deg, var(--nav-active-top), var(--nav-active-bottom)); color: var(--nav-active-text); font-size: 20px; font-weight: 600; }

  .brand { position: absolute; left: 18px; top: 790px; display: flex; align-items: center; gap: 14px; color: var(--text); font-size: 22px; }
  .brand__mark { width: 40px; height: 40px; background: var(--text); }

  .footer { position: absolute; left: 0; top: 900px; width: 1200px; height: 60px; background: var(--footer); }
</style>
</head>
<body>
<div class="page">
  <div class="gallery">
    <div class="photo photo--house1" role="img" aria-label="Foto: Backsteinhaus mit Garten"></div>
    <div class="photo photo--house2" role="img" aria-label="Foto: weißes Einfamilienhaus"></div>
    <div class="photo photo--house3" role="img" aria-label="Foto: Haus mit rotem Dach hinter Bäumen"></div>
    <div class="photo photo--office" role="img" aria-label="Foto: Bürogebäude mit Glasfassade"></div>
    <div class="photo photo--tower" role="img" aria-label="Foto: Glasturm vor blauem Himmel"></div>
    <div class="photo photo--winter" role="img" aria-label="Foto: Fachwerkhaus im Schnee"></div>
    <div class="band"></div>
  </div>

  <div class="claim">
    <h1 class="claim__script claim__headline">Architekten schaffen</h1>
    <p class="claim__line claim__line--raum">Lebens - Raum</p>
    <p class="claim__line claim__line--traum">Lebens - Traum</p>
    <p class="claim__script claim__final">Traum Haus</p>
  </div>

  <ul class="nav">
    <li class="nav__item" style="top:0">Navigation</li>
    <li class="nav__item nav__item--active" style="top:66px">Nav-aktiv</li>
    <li class="nav__item" style="top:131px">Navigation</li>
    <li class="nav__item" style="top:197px">Navigation</li>
    <li class="nav__item" style="top:263px">Navigation</li>
    <li class="nav__item" style="top:329px">Navigation</li>
  </ul>

  <div class="brand">
    <span class="brand__mark"></span>
    <span class="brand__name">Planungsbüro Anton Weidler</span>
  </div>

  <div class="footer"></div>
</div>
</body>
</html>
```